Author needs a new book, Kindle and Audiobook cover design

I updated and re-edited a book I wrote 25 years ago but now realize the title and design did not get the job done. I am seeking a book, Kindle and audiobook design that will make me stand out. The final design will pop while being sensitive to the nature of the subject. The title of the book is Hollow Altars. Subtitle: Leaving Cold Pews Behind and Mending a Wounded Heart Along the Road by Delia R. Marwick. I am wanting to get the attention of people who have been damaged by a church relationship that started well but ended badly.
Updates

The book title is: Hollow Altars. The Subtitle is: Leaving Cold Pews Behind and Mending a Wounded Heart Along The Road. The dimension is 6x9 (150 pages) and I am the author: Delia R. Marwick

Target Market(s)

People with a church experience; church leadership. Religious abuse victims.

Industry/Entity Type

Christian

Font styles to use
Serif

Colors

Designer to choose colors to be used in the design.

Requirements
Nice to have
• I am not married to the Serif font if another design works better.

```html
<!DOCTYPE html>
<html lang="en">
<head>
<meta charset="utf-8">
<title>Hollow Altars – Cover Wrap</title>
<link href="https://fonts.googleapis.com/css2?family=Jost:wght@300;400&family=Arimo:ital@0;1&display=swap" rel="stylesheet">
<style>
  :root {
    --page: #ffffff;
    --bleed: #f3f0e0;
    --ink: #050505;
    --paper-white: #ffffff;
    --band-navy: #1e2f52;
    --band-teal: #14827a;
    --photo-light: #8a8a8a;
    --photo-dark: #111111;
  }
  * { box-sizing: border-box; margin: 0; padding: 0; }
  html, body { width: 1200px; height: 874px; overflow: hidden; background: var(--page); }
  .wrap {
    position: absolute; left: 38px; top: 27px; width: 1118px; height: 820px;
    background: var(--bleed); padding: 10px;
    box-shadow: 0 2px 10px rgba(0,0,0,.25);
  }
  .sheet { position: relative; width: 100%; height: 100%; background: var(--ink); overflow: hidden; color: var(--paper-white); }

  /* back cover */
  .back { position: absolute; left: 0; top: 0; width: 527px; height: 100%; }
  .back-photo {
    position: absolute; left: 0; top: 300px; width: 527px; height: 500px;
    background: radial-gradient(ellipse at 40% 55%, rgba(120,120,120,.35), rgba(0,0,0,0) 65%);
  }
  .blurb { position: absolute; left: 45px; width: 440px; text-align: center; font-family: "Arimo", Arial, sans-serif; }
  .blurb-quote { font-style: italic; font-size: 12.6px; line-height: 17.5px; }
  .blurb-source { font-size: 12.6px; line-height: 17px; margin-top: 10px; }
  .divider { position: absolute; left: 45px; top: 616px; width: 440px; height: 1px; background: var(--paper-white); }
  .author-portrait {
    position: absolute; left: 58px; top: 640px; width: 126px; height: 126px; border-radius: 50%;
    background: radial-gradient(circle at 50% 45%, #c99a86, #6b5a55 70%); border: 4px solid #8a8580;
  }
  .bio { position: absolute; left: 196px; top: 652px; width: 300px; font-family: "Arimo", Arial, sans-serif; font-size: 12.6px; line-height: 16.5px; }

  /* spine */
  .spine { position: absolute; left: 527px; top: 0; width: 40px; height: 100%; }
  .spine-text { position: absolute; left: 0; width: 40px; writing-mode: vertical-rl; font-family: "Jost", sans-serif; font-weight: 300; display: flex; align-items: center; }
  .spine-author { top: 78px; font-size: 15px; letter-spacing: 9px; }
  .spine-title { top: 400px; font-size: 18px; letter-spacing: 10px; }

  /* front cover */
  .front { position: absolute; left: 567px; top: 0; width: 531px; height: 100%; }
  .front-photo {
    position: absolute; left: 0; top: 0; width: 531px; height: 540px;
    background: radial-gradient(ellipse at 58% 40%, var(--photo-light) 0%, #3a3a3a 35%, var(--photo-dark) 70%);
  }
  .title { position: absolute; left: 0; width: 100%; text-align: center; font-family: "Jost", sans-serif; font-weight: 300; font-size: 52px; letter-spacing: 19px; line-height: 1; }
  .title-first { top: 442px; }
  .title-second { top: 506px; }
  .subtitle-band {
    position: absolute; left: 0; top: 592px; width: 531px; height: 78px;
    background: linear-gradient(90deg, var(--band-navy), var(--band-teal));
    display: flex; align-items: center; justify-content: center; text-align: center;
    font-family: "Arimo", Arial, sans-serif; font-size: 15px; line-height: 30px; padding: 0 30px;
  }
  .front-author { position: absolute; left: 0; top: 731px; width: 100%; text-align: center; font-family: "Jost", sans-serif; font-size: 15px; letter-spacing: 7px; }
</style>
</head>
<body>
<div class="wrap">
  <div class="sheet">
    <section class="back">
      <div class="back-photo" role="img" aria-label="Faint photo of clasped praying hands"></div>

      <div class="blurb" style="top:38px">
        <p class="blurb-quote">Delia Marwick offers expert insight and a transparent evaluation in this book. With years of healthy involvement with that which is right in the body of Christ, she can speak to both the personal and systematic issues that cause bad environments to develop. The church landscape is littered with people who have been hurt in churches. This book will help clean things up.</p>
        <p class="blurb-source">--Warren Pellham, Senior Pastor, Cedar Hill Fellowship, Aldenbrook, VT.<br>Cedarhillfc.org</p>
      </div>

      <div class="blurb" style="top:208px">
        <p class="blurb-quote">“Seldom, if ever, have<br>I read a book that was so refreshingly personal and real, yet delivered material that put you in a position to navigate the difficult and damaging challenges, of being part of a degenerating church. I was moved to tears and then lifted to a place of hope, by the pain and abuse that this family faced and their</p>
        <p class="blurb-source">-- Marta Okonjo, Kestrel Ministries, kestrelmissionjourney.com</p>
      </div>

      <div class="blurb" style="top:366px">
        <p class="blurb-quote">“Delia Marwick offers a real-world view on how following your spiritual calling is not always easy but completely worth the journey. Her down to earth approach allows the reader to process and be encouraged by her personal story, insight, and commitment to faith.”</p>
        <p class="blurb-source">-- Renee Dalworth, Executive Director, OPENDOOR Outreach, Inc. Opendoorout.org</p>
      </div>

      <div class="blurb" style="top:478px">
        <p class="blurb-quote">“Delia Marwick has been a pastor over 40 years. I have known her personally for many of those years. This book is a case study of how trust can be abused. Delia handles this difficult issue with a good balance of honest introspection and critical analysis of leadership structures and practices. This book is a must-read.”</p>
        <p class="blurb-source">-- --Gerald P. Ashcombe, FaithReasonDesk.com</p>
      </div>

      <div class="divider"></div>
      <div class="author-portrait" role="img" aria-label="Author portrait photo"></div>
      <p class="bio">Delia Marwick is a long-time pastor, author and podcaster who has impacted leaders and churches for many years. She wrote Iceberg Ahead, a study of church leadership drawn from the history of the legendary ship. She and her husband Tom, together with their grown children and spouses all serve in ministry.</p>
    </section>

    <section class="spine">
      <div class="spine-text spine-author">Delia R. Marwick</div>
      <div class="spine-text spine-title">HOLLOW ALTARS</div>
    </section>

    <section class="front">
      <div class="front-photo" role="img" aria-label="Black and white photo of weathered hands clasped in prayer"></div>
      <h1 class="title title-first">HOLLOW</h1>
      <div class="title title-second">ALTARS</div>
      <div class="subtitle-band">Leaving Cold Pews Behind and Mending a Wounded Heart Along The Road</div>
      <div class="front-author">Delia R. Marwick</div>
    </section>
  </div>
</div>
</body>
</html>
```